brisknest

i want to ues this logo and the same colors used on the business card

cleaning & service

Industry/Entity Type

Business

Contact Information for Business Card

Font styles to use
Serif
Sans Serif
Decorative
Script

Colors
add136
0692cd
000000
5c5c5c
fbfbfb

Requirements
Must have
• cleaning things

```html
<!DOCTYPE html>
<html lang="en">
<head>
<meta charset="UTF-8">
<title>brisknest business card</title>
<link rel="stylesheet" href="https://fonts.googleapis.com/css2?family=Montserrat:wght@400;500;700&display=swap">
<style>
  :root {
    --blue: #0a74bf;
    --green: #add136;
    --card: #f3f7ea;
    --ink: #5c5c5c;
    --white: #fbfbfb;
    --backdrop: #2a2a2a;
  }
  * { margin: 0; padding: 0; box-sizing: border-box; }
  html, body {
    width: 1200px;
    height: 900px;
    overflow: hidden;
    background: var(--backdrop);
    font-family: "Montserrat", Arial, sans-serif;
  }
  .stage {
    position: relative;
    width: 1200px;
    height: 900px;
  }
  .card {
    position: absolute;
    left: 250px;
    width: 700px;
    height: 400px;
    background: var(--card);
    overflow: hidden;
    box-shadow: 0 10px 30px rgba(0,0,0,0.5);
  }
  .card--front { top: 35px; }
  .card--back { top: 465px; }

  .band {
    position: absolute;
    background: var(--blue);
  }
  .card--front .band {
    left: 0;
    top: 150px;
    width: 390px;
    height: 78px;
  }
  .card--back .band {
    left: 0;
    top: 120px;
    width: 700px;
    height: 82px;
  }

  .brand {
    position: absolute;
    display: flex;
    align-items: center;
    gap: 10px;
  }
  .brand__dot {
    width: 18px;
    height: 18px;
    border-radius: 50%;
    background: var(--green);
  }
  .brand__name {
    font-weight: 700;
    font-size: 34px;
    color: var(--blue);
    letter-spacing: 0.5px;
  }
  .card--front .brand { left: 440px; top: 150px; }
  .card--back .brand { left: 460px; top: 250px; }
  .card--back .brand__name { font-size: 30px; }

  .person {
    position: absolute;
    left: 60px;
    top: 138px;
    color: var(--white);
  }
  .person__name {
    font-weight: 700;
    font-size: 22px;
    letter-spacing: 0.3px;
    text-transform: uppercase;
  }
  .person__surname { color: var(--green); }
  .person__role {
    font-weight: 400;
    font-size: 16px;
    margin-top: 2px;
  }

  .contact {
    position: absolute;
    left: 70px;
    top: 232px;
    list-style: none;
    color: var(--ink);
    font-size: 17px;
  }
  .contact__item {
    display: flex;
    align-items: center;
    gap: 12px;
    margin-bottom: 12px;
  }
  .contact__icon { width: 16px; height: 16px; flex: none; }
</style>
</head>
<body>
<main class="stage">
  <section class="card card--front" aria-label="Card front">
    <div class="band"></div>
    <div class="brand">
      <span class="brand__dot"></span>
      <span class="brand__name">brisknest</span>
    </div>
  </section>

  <section class="card card--back" aria-label="Card back">
    <div class="band"></div>
    <div class="person">
      <p class="person__name">Maren <span class="person__surname">Holloway</span></p>
      <p class="person__role">General Manager</p>
    </div>
    <ul class="contact">
      <li class="contact__item">
        <svg class="contact__icon" viewBox="0 0 24 24" aria-hidden="true">
          <path fill="#add136" d="M6.6 10.8c1.4 2.8 3.8 5.1 6.6 6.6l2.2-2.2c.3-.3.7-.4 1-.2 1.1.4 2.3.6 3.6.6.6 0 1 .4 1 1V20c0 .6-.4 1-1 1C10.6 21 3 13.4 3 4c0-.6.4-1 1-1h3.5c.6 0 1 .4 1 1 0 1.3.2 2.5.6 3.6.1.3 0 .7-.2 1l-2.3 2.2z"/>
        </svg>
        <span>(780) 555-0143</span>
      </li>
      <li class="contact__item">
        <svg class="contact__icon" viewBox="0 0 24 24" aria-hidden="true">
          <rect x="2" y="5" width="20" height="14" rx="1.5" fill="#add136"/>
          <path d="M3 6l9 7 9-7" fill="none" stroke="#f3f7ea" stroke-width="1.8"/>
        </svg>
        <span>maren.brisknest@mail.com</span>
      </li>
    </ul>
    <div class="brand">
      <span class="brand__dot"></span>
      <span class="brand__name">brisknest</span>
    </div>
  </section>
</main>
</body>
</html>
```